Law Firm Business Card

This is a business card for a law firm that serves US military and veterans.

The card must have ONLY the following (we want an uncluttered look):

- Company logo (PNG, GIF, JPEG copies uploaded)
- A tagline reading: "a law firm for service members and veterans"
- My name and title: "Martin Okello" and "Attorney"
- My email: "martin.okello@harborlinecounsel.com"
- My number: "855-FILE-NOW (345-3669)"

We are looking for a clean, simple layout with only the above information, likely printed on a bright white cotton stock. The font of our logo is DIN 1451, and the font used on our website is Helvetica Neue. The color of our logo is #336699, and we probably want the tagline in that color also, and my contact information in a dark grey. Please review our website at www.harborlinecounsel.com to ensure your card design complements our website style.

Thanks and we look forward to seeing your submissions.

A few notes:

- Two-sided submissions are ok
- Please don't add graphics (scales of justice, judges hammer, etc)

```html
<!DOCTYPE html>
<html lang="en">
<head>
<meta charset="utf-8">
<title>Harborline Counsel – Business Card</title>
<link rel="stylesheet" href="https://fonts.googleapis.com/css2?family=Barlow+Condensed:wght@500;600&family=Barlow:wght@400;500&family=Crimson+Text&display=swap">
<style>
  :root {
    --brand-blue: #336699;
    --card-white: #ffffff;
    --ink-dark: #333333;
    --ink-black: #111111;
    --divider: #c9c9c9;
    --backdrop: #ece9e4;
  }
  * { margin: 0; padding: 0; box-sizing: border-box; }
  html, body {
    width: 1200px;
    height: 952px;
    overflow: hidden;
    background: var(--backdrop);
  }
  .canvas {
    position: relative;
    width: 1200px;
    height: 952px;
  }
  .card {
    position: absolute;
    width: 640px;
    height: 366px;
    box-shadow: 0 6px 18px rgba(0, 0, 0, 0.18);
  }

  /* Front */
  .card-front {
    left: 60px;
    top: 70px;
    background: var(--card-white);
  }
  .wordmark {
    font-family: "Barlow Condensed", sans-serif;
    font-weight: 600;
    color: var(--brand-blue);
    text-transform: uppercase;
    line-height: 0.95;
    letter-spacing: 0.02em;
  }
  .card-front .wordmark {
    position: absolute;
    left: 40px;
    top: 50px;
    font-size: 44px;
  }
  .tagline {
    position: absolute;
    left: 40px;
    bottom: 38px;
    font-family: "Crimson Text", serif;
    font-size: 17px;
    line-height: 1.2;
    color: var(--brand-blue);
  }
  .divider {
    position: absolute;
    left: 350px;
    top: 200px;
    width: 1px;
    height: 130px;
    background: var(--divider);
    box-shadow: 2px 0 3px rgba(0, 0, 0, 0.12);
  }
  .contact-block {
    position: absolute;
    left: 372px;
    top: 204px;
    font-family: "Barlow", sans-serif;
  }
  .contact-name {
    font-size: 19px;
    font-weight: 500;
    color: var(--brand-blue);
  }
  .contact-title {
    font-size: 14px;
    color: var(--ink-black);
    margin-top: 2px;
    margin-left: 6px;
  }
  .contact-list {
    list-style: none;
    margin-top: 18px;
    margin-left: 6px;
  }
  .contact-list li {
    display: flex;
    align-items: center;
    gap: 7px;
    font-size: 13.5px;
    color: var(--ink-dark);
    margin-bottom: 7px;
    white-space: nowrap;
  }
  .contact-list svg {
    width: 13px;
    height: 13px;
    flex: none;
  }

  /* Back */
  .card-back {
    left: 500px;
    top: 516px;
    background: var(--brand-blue);
    display: flex;
    align-items: center;
    justify-content: center;
  }
  .card-back .wordmark {
    color: var(--card-white);
    font-size: 78px;
    text-align: center;
  }
</style>
</head>
<body>
<main class="canvas">

  <section class="card card-front" aria-label="Business card front">
    <div class="wordmark">Harborline<br>Counsel</div>

    <p class="tagline">A Law Firm<br>For Service Members &amp; Veterans</p>

    <span class="divider"></span>

    <div class="contact-block">
      <p class="contact-name">Martin Okello</p>
      <p class="contact-title">Attorney</p>
      <ul class="contact-list">
        <li>
          <svg viewBox="0 0 16 16" aria-hidden="true"><circle cx="8" cy="8" r="7" fill="none" stroke="#336699" stroke-width="1.4"/><path d="M6 4.5c-.8.4-1 1.4-.6 2.6.5 1.6 1.8 3.4 3.3 4.3.9.5 1.6.4 2-.2l-1.3-1.4-.9.5c-.8-.5-1.5-1.5-1.8-2.4l.8-.6z" fill="#336699"/></svg>
          855-FILE-NOW (345-3669)
        </li>
        <li>
          <svg viewBox="0 0 16 16" aria-hidden="true"><rect x="1" y="4" width="14" height="9" fill="#336699"/><path d="M1 4l7 5 7-5" fill="none" stroke="#fff" stroke-width="1.2"/></svg>
          martin.okello@harborlinecounsel.com
        </li>
        <li>
          <svg viewBox="0 0 16 16" aria-hidden="true"><g fill="none" stroke="#336699" stroke-width="1.2"><circle cx="8" cy="8" r="6.5"/><ellipse cx="8" cy="8" rx="3" ry="6.5"/><path d="M1.5 8h13M2.5 5h11M2.5 11h11"/></g></svg>
          www.harborlinecounsel.com
        </li>
      </ul>
    </div>
  </section>

  <section class="card card-back" aria-label="Business card back">
    <div class="wordmark">Harborline<br>Counsel</div>
  </section>

</main>
</body>
</html>
```